Redesign of Bright Harbor Entertainment Card

I already have my logo and font design for my company name. I am looking to come up with a Unique way of having it on my business card. Just looking for a really hip, and professional business card while still using my logo design.

I have also enclosed the front and back of the card so you can see what I have now. Looking for something different.

Thank you!

Target Market(s)

Young to middle aged brides and grooms

Industry/Entity Type

Business

Requirements
Should not have
• Cheese

```html
<!DOCTYPE html>
<html lang="en">
<head>
<meta charset="utf-8">
<title>Bright Harbor Entertainment – Business Card</title>
<link href="https://fonts.googleapis.com/css2?family=Oswald:wght@300;400&family=Open+Sans:wght@400&display=swap" rel="stylesheet">
<style>
  :root {
    --backdrop: #e4e5e7;
    --card: #f7f7f5;
    --card-shadow: rgba(40, 44, 52, 0.18);
    --navy-blue: #1f3fae;
    --sky-blue: #2aa3d8;
    --panel-blue: #d9eef5;
    --watermark: #e6e6e4;
  }
  * { margin: 0; padding: 0; box-sizing: border-box; }
  html, body {
    width: 1200px;
    height: 1000px;
    overflow: hidden;
    background: var(--backdrop);
  }
  .canvas {
    position: relative;
    width: 1200px;
    height: 1000px;
  }
  .business-card {
    position: absolute;
    left: 250px;
    width: 700px;
    height: 400px;
    background: var(--card);
    box-shadow: 0 6px 18px var(--card-shadow);
    overflow: hidden;
  }
  .card-contact { top: 60px; }
  .card-brand { top: 540px; }

  /* Contact side */
  .watermark-disc {
    position: absolute;
    left: 230px;
    top: 55px;
    width: 240px;
    height: 240px;
    border-radius: 50%;
    background: var(--watermark);
  }
  .contact-block {
    position: absolute;
    left: 0;
    right: 0;
    top: 120px;
    text-align: center;
  }
  .contact-name,
  .contact-email {
    font-family: "Oswald", sans-serif;
    font-weight: 300;
    color: var(--navy-blue);
    font-size: 30px;
    line-height: 38px;
  }
  .contact-details {
    margin-top: 20px;
    font-family: "Open Sans", sans-serif;
    color: var(--sky-blue);
    font-size: 17px;
    line-height: 23px;
  }

  /* Brand side */
  .services-panel {
    position: absolute;
    top: 0;
    right: 0;
    width: 260px;
    height: 170px;
    background: var(--panel-blue);
    border-bottom-left-radius: 22px;
    padding: 18px 26px 0 0;
    text-align: right;
  }
  .services-list {
    list-style: none;
    font-family: "Oswald", sans-serif;
    font-weight: 300;
    color: var(--navy-blue);
    font-size: 26px;
    line-height: 33px;
  }
  .brand-lockup {
    position: absolute;
    left: 40px;
    bottom: 48px;
    display: flex;
    align-items: center;
    gap: 16px;
  }
  .brand-dot {
    width: 64px;
    height: 64px;
    border-radius: 50%;
    background: var(--navy-blue);
  }
  .brand-name {
    font-family: "Oswald", sans-serif;
    font-weight: 400;
    color: var(--navy-blue);
    font-size: 52px;
    line-height: 1;
    text-transform: uppercase;
    letter-spacing: 2px;
  }
</style>
</head>
<body>
<main class="canvas">
  <section class="business-card card-contact" aria-label="Business card, contact side">
    <div class="watermark-disc" aria-hidden="true"></div>
    <div class="contact-block">
      <p class="contact-name">DJ Mark Ellery</p>
      <p class="contact-email">info@brightharbor.com</p>
      <div class="contact-details">
        <p>555 - 019 - DJDJ</p>
        <p>brightharbor.com</p>
        <p>facebook.com/brightharborentertainment</p>
      </div>
    </div>
  </section>

  <section class="business-card card-brand" aria-label="Business card, brand side">
    <div class="services-panel">
      <ul class="services-list">
        <li>DJs/Emcees</li>
        <li>LED Uplighting</li>
        <li>Photo Booths</li>
        <li>Photo Montages</li>
      </ul>
    </div>
    <div class="brand-lockup">
      <span class="brand-dot" aria-hidden="true"></span>
      <span class="brand-name">Bright Harbor</span>
    </div>
  </section>
</main>
</body>
</html>
```